Etiketten für prämierte BBQ Sauce
tr Grafikstube arbeitet sehr professionell und ist sehr hilfsbereit
Zielgruppe
Wir sind ein junges erfolgreiches BBQ Team und suchen für unsere prämierte Sauce ein Etikett.
Aufgabenstellung
Es ist eine Flasche mit 263 ml, der Umfang ist 18 cm, Höhe für das Etikett 6cm (wobei anhand der Aussparung 5.8 besser wäre). Es muss nicht die ganze Flasche umschliessen
Deckel max. 2.6 im Durchmesser
Folgende Infos müssen ersichtlich sein
Honey Mustard Sauce
263ml
Zutatenliste: Senf, Honig, Ketchup, Gewürze, Zucker, Natürliche Aromen, Essig
Mindesthaltbarkeit
Nach dem Öffnen im Kühlschrank aufbewahren
Like us on Plaudernet
Es wäre schön, wenn sich das Logo im Etikett einbetten würde, muss aber nicht. Jedoch sollte es dann zumindest irgendwo bei den Zutaten oder so ersichtlich sein. Mir persönlich schwebte mal etwas im Stil von Kreide vor so quasi das Logo monochrom mit Kreide. Jedoch ist das auch kein muss es soll aber aufzeigen, dass das Logo auch schwarz/weiss sein darf. Dies ist nur mal eine Idee welche ich hatte aber ich überlasse der Creativen Crowd die Freiheit das Etikett zu gestalten :-)
Bei Fragen einfach melden

```html
<!DOCTYPE html>
<html lang="de">
<head>
<meta charset="utf-8">
<title>Feuerlurch BBQ – Honey Mustard Sauce Etikett</title>
<link href="https://fonts.googleapis.com/css2?family=Archivo+Narrow:wght@400;700&family=Rye&family=Josefin+Sans:wght@400&display=swap" rel="stylesheet">
<style>
  :root {
    --page: #eceff1;
    --board: #2e2f30;
    --board-edge: #262728;
    --chalk: #d8d8d8;
    --chalk-soft: #bdbdbd;
    --mustard: #8f9a2c;
    --mustard-light: #b4bd4f;
  }
  * { margin: 0; padding: 0; box-sizing: border-box; }
  html, body { width: 1200px; height: 1085px; overflow: hidden; }
  body {
    background: var(--page);
    position: relative;
    font-family: "Archivo Narrow", Arial, sans-serif;
  }
  .label {
    position: absolute;
    left: 0; top: 348px;
    width: 1200px; height: 388px;
    background: radial-gradient(ellipse at 40% 40%, var(--board) 0%, var(--board-edge) 100%);
    overflow: hidden;
    color: var(--chalk);
  }
  .brand-mark {
    position: absolute;
    left: 140px; top: 130px;
    width: 300px;
    display: flex; align-items: center; justify-content: center; gap: 12px;
  }
  .brand-mark .dot {
    width: 26px; height: 26px; border-radius: 50%;
    background: var(--chalk-soft);
    flex: none;
  }
  .brand-mark .name {
    font-family: "Archivo Narrow", Arial, sans-serif;
    font-weight: 700; font-size: 38px; color: var(--chalk-soft);
    line-height: 1.05; white-space: nowrap;
  }
  .product-title {
    position: absolute; left: 90px; top: 274px; width: 400px;
    text-align: center;
    font-family: "Rye", Georgia, serif;
    font-size: 40px; color: var(--mustard);
    line-height: 1; white-space: nowrap;
  }
  .product-type {
    position: absolute; left: 90px; top: 320px; width: 400px;
    text-align: center;
    font-family: "Josefin Sans", Arial, sans-serif;
    font-size: 24px; line-height: 28px; letter-spacing: 10px; color: var(--chalk-soft);
    padding-left: 10px;
  }
  .volume {
    position: absolute; left: 474px; top: 338px;
    font-family: "Rye", Georgia, serif; font-size: 15px; line-height: 18px; color: var(--chalk-soft);
  }
  .grass-band {
    position: absolute; left: 0; bottom: 0; width: 1200px; height: 30px;
    display: block;
  }
  .info {
    position: absolute; left: 611px; top: 36px; width: 600px;
    text-align: center; font-size: 17px; line-height: 23px; color: var(--chalk);
    white-space: nowrap;
  }
  .info h2 {
    font-family: "Rye", Georgia, serif; font-weight: 400;
    font-size: 19px; color: var(--chalk); line-height: 26px;
  }
  .info .ingredients-title { margin-top: 16px; }
  .info .social { margin-top: 18px; }
  .info .best-before { margin-top: 42px; font-size: 18px; }
</style>
</head>
<body>
  <section class="label" aria-label="Flaschenetikett Honey Mustard Sauce">
    <div class="brand-mark">
      <span class="dot"></span>
      <span class="name">Feuerlurch BBQ</span>
    </div>
    <div class="product-title">Honey Mustard</div>
    <div class="product-type">SAUCE</div>
    <div class="volume">263ml</div>

    <svg class="grass-band" role="img" aria-label="Gelbgrünes Kreide-Wellenband als Fußleiste" viewBox="0 0 1200 30" preserveAspectRatio="none">
      <defs>
        <linearGradient id="band-fill" x1="0" y1="0" x2="0" y2="1">
          <stop offset="0" stop-color="#b4bd4f"/>
          <stop offset="1" stop-color="#8f9a2c"/>
        </linearGradient>
      </defs>
      <path d="M0 14 C60 6 110 6 170 12 S280 20 340 12 S440 6 480 16 S540 24 600 14 S700 4 760 12 S860 20 920 10 S1020 4 1080 12 S1160 18 1200 10 V30 H0 Z" fill="url(#band-fill)"/>
    </svg>

    <div class="info">
      <h2>Feuerlurch BBQ</h2>
      <p>Beschreibungstext Lorem ipsum dolor sit amet, consetetur sadipscing elitr,<br>
      sed diam nonumy eirmod tempor invidunt ut labore et dolore magna aliquyam<br>
      erat, sed diam voluptua. At vero eos et accusam et justo duo dolores et ea rebum.</p>
      <h2 class="ingredients-title">Zutatenliste:</h2>
      <p>Senf, Honig, Ketchup, Gewürze, Zucker, Natürliche Aromen, Essig</p>
      <h2 class="social">Like us on Plaudernet</h2>
      <p class="best-before">Mindesthaltbarkeit 08/2018</p>
      <p>Nach dem Öffnen im Kühlschrank aufbewahren</p>
    </div>
  </section>
</body>
</html>
```